Fr. K Winery Wine Label Design

We are looking to redesign our wine labels. i have updated this contest to focus on just the premium wines. These should have gold writing on a silk screened bottle, or on black traditional label. Red or gold capsule.
Our logo is of a mountain with dated cursive script (see attached). We are hoping to maintain some of that brand identity but with a more premium look. The current cursive script definitely needs to be altered. Fennick K is an extinct volcano that is a local landmark in the Okanagan Valley. One concept was using this image as a background or element of the labels or a new logo. i have attached an actual photo of the mountain. This is only to inspire a simplified logo.

Target Market(s)

30-65

Logo Text

Fr. (or Fennick) Larrowet

Font styles to use
Serif
Script

Colors
1b1b1b
ec1f27
fbf289

Requirements
Must have
• High End Feel. silkscreen? gold writing. wine is called "Harbor"
Nice to have
• "estate grown"

```html
<!DOCTYPE html>
<html lang="en">
<head>
<meta charset="utf-8">
<title>Fennick K — Harbor Super Premium Label</title>
<link href="https://fonts.googleapis.com/css2?family=Cinzel:wght@400;500&display=swap" rel="stylesheet">
<style>
  :root {
    --canvas-bg: #ffffff;
    --label-black: #050607;
    --gold: #e2a822;
    --gold-line: #d99c1c;
  }
  html, body {
    margin: 0;
    padding: 0;
    width: 1200px;
    height: 1000px;
    overflow: hidden;
    background: var(--canvas-bg);
  }
  .canvas {
    position: relative;
    width: 1200px;
    height: 1000px;
  }
  .wine-label {
    position: absolute;
    left: 380px;
    top: 135px;
    width: 439px;
    height: 730px;
    display: block;
  }
  .label-ground { fill: var(--label-black); }
  .label-frame { fill: none; stroke: var(--gold-line); stroke-width: 2; }
  .label-text {
    fill: var(--gold);
    font-family: "Cinzel", "Trajan Pro", serif;
    font-weight: 400;
  }
  .brand-name { font-size: 58px; }
  .wine-name { font-size: 52px; letter-spacing: 1px; }
  .wine-grade { font-size: 25px; letter-spacing: 0.5px; }
  .abv { font-size: 17px; }
  .abv-unit { font-size: 10px; }
  .volume { font-size: 26px; }
</style>
</head>
<body>
<main class="canvas">
  <svg class="wine-label" viewBox="0 0 439 730" xmlns="http://www.w3.org/2000/svg" aria-label="Fennick K Harbor Super Premium wine label">
    <rect class="label-ground" x="0" y="0" width="439" height="730"/>

    <g class="label-border">
      <rect class="label-frame" x="37" y="11" width="365" height="708"/>
      <rect class="label-frame" x="24" y="23" width="391" height="684"/>
      <rect class="label-frame" x="17" y="18" width="11" height="11"/>
      <rect class="label-frame" x="411" y="18" width="11" height="11"/>
      <rect class="label-frame" x="17" y="701" width="11" height="11"/>
      <rect class="label-frame" x="411" y="701" width="11" height="11"/>
    </g>

    <text class="label-text brand-name" x="219.5" y="308" text-anchor="middle">Fennick K</text>

    <text class="label-text wine-name" x="219.5" y="556" text-anchor="middle">Harbor</text>
    <text class="label-text wine-grade" x="219.5" y="594" text-anchor="middle">SUPER PREMIUM</text>

    <text class="label-text abv" x="68" y="698">12% <tspan class="abv-unit">VOL</tspan></text>
    <text class="label-text volume" x="381" y="698" text-anchor="end">750ML</text>
  </svg>
</main>
</body>
</html>
```